Carrow Equity Webinar Ads

Need a banner pack in less than 48 hours for this website:
http://carrowequity-example.com/webinar
Target Market(s)
Accredited real estate investors looking to grow their portfolio
Font styles to use
Sans Serif
Colors
0255a3
f37123
000000

```html
<!DOCTYPE html>
<html lang="en">
<head>
<meta charset="utf-8">
<title>Carrow Equity Webinar Banner</title>
<link href="https://fonts.googleapis.com/css2?family=Roboto:wght@500;700;900&display=swap" rel="stylesheet">
<style>
  :root {
    --brand-blue: #0255a3;
    --brand-orange: #f37123;
    --ink: #000000;
    --paper: #ffffff;
    --mist: #eef1f5;
    --stripe-grey: #c9d0d8;
  }
  html, body {
    margin: 0;
    padding: 0;
    overflow: hidden;
    background: var(--paper);
  }
  .banner {
    position: relative;
    width: 1200px;
    height: 148px;
    overflow: hidden;
    background: linear-gradient(90deg, var(--paper) 0%, var(--paper) 40%, var(--mist) 60%);
    font-family: "Roboto", Arial, sans-serif;
  }
  .audience-photo {
    position: absolute;
    left: 690px;
    top: 0;
    width: 510px;
    height: 148px;
    background:
      radial-gradient(ellipse at 30% 80%, rgba(120,60,50,0.55), transparent 60%),
      radial-gradient(ellipse at 70% 30%, rgba(190,190,195,0.8), transparent 55%),
      linear-gradient(100deg, #6b6b70 0%, #9a9a9e 40%, #b7b4b2 70%, #8c8a88 100%);
  }
  .photo-edge {
    position: absolute;
    left: 0;
    top: 0;
    width: 1200px;
    height: 148px;
    pointer-events: none;
  }
  .brand {
    position: absolute;
    left: 28px;
    top: 0;
    height: 148px;
    display: flex;
    align-items: center;
    gap: 10px;
  }
  .brand-mark {
    width: 22px;
    height: 22px;
    border-radius: 50%;
    background: var(--brand-blue);
  }
  .brand-name {
    font-weight: 700;
    font-size: 26px;
    color: var(--brand-blue);
    white-space: nowrap;
  }
  .headline {
    position: absolute;
    left: 300px;
    top: 29px;
    margin: 0;
    font-weight: 900;
    font-size: 25px;
    line-height: 30px;
    letter-spacing: 0.2px;
    color: var(--brand-blue);
    text-transform: uppercase;
  }
  .cta-button {
    position: absolute;
    left: 885px;
    top: 51px;
    width: 278px;
    height: 56px;
    display: flex;
    align-items: center;
    justify-content: center;
    background: var(--brand-orange);
    color: var(--paper);
    font-weight: 500;
    font-size: 22px;
    text-decoration: none;
  }
</style>
</head>
<body>
  <div class="banner">
    <div class="audience-photo" role="img" aria-label="Blurred photo of an audience seated in a conference hall"></div>
    <svg class="photo-edge" viewBox="0 0 1200 148" aria-hidden="true">
      <path d="M560 0 H700 Q650 74 690 148 H560 Z" fill="var(--mist)"/>
      <path d="M700 0 Q650 74 690 148" fill="none" stroke="var(--stripe-grey)" stroke-width="10"/>
      <path d="M712 0 Q664 74 702 148" fill="none" stroke="var(--brand-blue)" stroke-width="6"/>
    </svg>
    <div class="brand">
      <span class="brand-mark"></span>
      <span class="brand-name">Carrow Equity</span>
    </div>
    <h1 class="headline">Learn how easy it is to<br>profit in this great market<br>before values go back up..</h1>
    <a class="cta-button" href="http://carrowequity-example.com/webinar">Register for the Webinar</a>
  </div>
</body>
</html>
```